Diesel Fitting/Mechanical Company Needs a new Business Card

We would like a new business card that showcases our logo and business information.

Industry/Entity Type

Business

Contact Information for Business Card

314 Wendale Street
PO Box 7581 CHARTERS TOWERS QLD 4820
Phone: 49312787 Fax: 49312688 Mobile: 0438915276 ABN: 63 519 087 342

Requirements
Must have
• The following email addresses:
• admin@tkservicing.com.au , sales@tkservicing.com.au , accounts@tkservicing.com.au , parts@tkservicing.com.au , office@tkservicing.com.au
• Also need to have the website: www.tkservicing.com.au

```html
<!DOCTYPE html>
<html lang="en">
<head>
<meta charset="utf-8">
<title>TK Servicing – Business Card</title>
<link rel="stylesheet" href="https://fonts.googleapis.com/css2?family=Aleo:wght@400;700&family=Montserrat:wght@400;700&display=swap">
<style>
  :root {
    --page-bg: #ffffff;
    --card-bg: #ffffff;
    --orange: #f07a2b;
    --ink: #1a1a1a;
    --yellow: #fcc21b;
    --shadow: rgba(0, 0, 0, 0.28);
  }
  html, body {
    margin: 0;
    padding: 0;
    width: 1200px;
    height: 1000px;
    overflow: hidden;
    background: var(--page-bg);
  }
  .canvas {
    position: relative;
    width: 1200px;
    height: 1000px;
  }
  .card {
    position: absolute;
    top: 306px;
    width: 421px;
    height: 271px;
    background: var(--card-bg);
    box-shadow: 2px 3px 5px var(--shadow);
    overflow: hidden;
  }
  .card--front { left: 152px; }
  .card--back { left: 627px; }

  .brand {
    position: absolute;
    left: 0;
    right: 0;
    top: 112px;
    display: flex;
    align-items: center;
    justify-content: center;
    gap: 14px;
  }
  .brand__dot {
    width: 22px;
    height: 22px;
    border-radius: 50%;
    background: var(--yellow);
  }
  .brand__name {
    font-family: "Montserrat", sans-serif;
    font-weight: 700;
    font-size: 36px;
    line-height: 1;
    color: var(--orange);
  }

  .website {
    position: absolute;
    left: 19px;
    top: 34px;
    writing-mode: vertical-rl;
    font-family: "Aleo", serif;
    font-size: 17px;
    color: var(--orange);
    letter-spacing: 0.2px;
  }
  .divider {
    position: absolute;
    left: 150px;
    top: 86px;
    width: 2px;
    height: 116px;
    background: var(--ink);
  }
  .emails {
    position: absolute;
    left: 168px;
    top: 90px;
    margin: 0;
    padding: 0;
    list-style: none;
    font-family: "Aleo", serif;
    font-size: 16px;
    line-height: 21px;
    color: var(--ink);
  }
  .emails__box {
    font-weight: 700;
    color: var(--orange);
  }
  .corner-accent {
    position: absolute;
    right: 0;
    bottom: 0;
    width: 55px;
    height: 70px;
  }

  .caption {
    position: absolute;
    left: 770px;
    top: 845px;
    margin: 0;
    font-family: "Montserrat", sans-serif;
    font-weight: 700;
    font-size: 24px;
    color: #111111;
  }
</style>
</head>
<body>
<main class="canvas">
  <section class="card card--front" aria-label="Card front">
    <div class="brand">
      <span class="brand__dot" aria-hidden="true"></span>
      <span class="brand__name">TK Servicing</span>
    </div>
  </section>

  <section class="card card--back" aria-label="Card back">
    <div class="website">www.tkservicing.com.au</div>
    <div class="divider" aria-hidden="true"></div>
    <ul class="emails">
      <li><span class="emails__box">admin</span>@tkservicing.com.au</li>
      <li><span class="emails__box">sales</span>@tkservicing.com.au</li>
      <li><span class="emails__box">accounts</span>@tkservicing.com.au</li>
      <li><span class="emails__box">parts</span>@tkservicing.com.au</li>
      <li><span class="emails__box">office</span>@tkservicing.com.au</li>
    </ul>
    <svg class="corner-accent" viewBox="0 0 55 70" aria-hidden="true">
      <polygon points="0,0 55,40 55,70 30,70" fill="var(--yellow)"/>
    </svg>
  </section>

  <p class="caption">TK Business card 1</p>
</main>
</body>
</html>
```